Flyer for IT Services

We need a flyer template for our different products and services we offer. We're an IT firm that provides Managed Services, Remote Backup, Mobile Device Management, Unified Communications, and more.

The flyer should be two sided and provide an area for an explanation of the service and then some pictures, lists of features, and a section for our contact info and company description.

We will normally send the flyer over to a client as a PDF via email but may also printer the flyers to hand out at meetings with prospects.

Information on the services to get ideas is at the following and the services heading:
www.tidewellsys.com

Target Market(s)

small to medium sized companies (2-150 employees)

Industry/Entity Type

Printer

Requirements
Must have
• Flyer must be two sided, include our logo, and have sections for product and company description as well as feature lists.

```html
<!DOCTYPE html>
<html lang="en">
<head>
<meta charset="utf-8">
<title>Tidewell Systems – IT Services Flyer</title>
<link rel="stylesheet" href="https://fonts.googleapis.com/css2?family=Open+Sans:wght@400;600&display=swap">
<style>
  :root {
    --stage: #1f2022;
    --blue: #1b86d6;
    --blue-deep: #1569b0;
    --navy: #103c61;
    --frame: #2196ea;
    --white: #ffffff;
    --grey-dark: #3a3b3d;
    --grey-mid: #5d5f62;
    --ink-soft: #e9f3fb;
  }
  * { box-sizing: border-box; margin: 0; padding: 0; }
  html, body { width: 1200px; height: 900px; overflow: hidden; background: var(--stage); }
  body { font-family: "Open Sans", sans-serif; color: var(--white); position: relative; }

  .page { position: absolute; top: 50px; width: 560px; height: 800px; overflow: hidden; }

  /* Front side */
  .page--front { left: 20px; border: 8px solid var(--frame); background: linear-gradient(180deg, var(--blue) 0%, var(--blue-deep) 100%); }
  .hero-photo { position: absolute; left: 0; top: 0; width: 100%; height: 300px;
    background: radial-gradient(circle at 28% 62%, #4aa6e6 0 14%, #1d5f9a 22%, transparent 34%),
                linear-gradient(135deg, #5a5d62 0%, #b9bcc0 45%, #e6e7e9 100%); }
  .hero-band { position: absolute; left: 0; top: 300px; width: 100%; height: 32px; background: var(--navy); }
  .about { position: absolute; left: 22px; right: 22px; top: 342px; z-index: 2; }
  .about__title { font-size: 29px; font-weight: 400; line-height: 1.3; margin-bottom: 12px; }
  .about__text { font-size: 15px; line-height: 1.42; margin-bottom: 16px; color: var(--ink-soft); }
  .front-foot { position: absolute; left: 0; bottom: 0; width: 100%; height: 120px; z-index: 1; }
  .brand { position: absolute; right: 30px; bottom: 24px; display: flex; align-items: center; gap: 12px; z-index: 2; }
  .brand__mark { width: 32px; height: 32px; border-radius: 50%; background: var(--blue-deep); }
  .brand__name { font-size: 38px; font-weight: 600; line-height: 1.1; color: var(--blue-deep); }

  /* Back side */
  .page--back { left: 620px; background: var(--blue); }
  .side-photo { position: absolute; left: 0; top: 0; width: 200px; height: 610px;
    background: linear-gradient(180deg, #2aa6ea 0%, #7cc8f2 45%, #cde9f8 75%, #9fd0ee 100%); }
  .contact { position: absolute; left: 0; top: 610px; width: 200px; height: 190px;
    background: linear-gradient(180deg, var(--grey-mid) 0%, var(--grey-dark) 100%); text-align: center; padding-top: 16px; }
  .contact__title { font-size: 22px; font-weight: 400; margin-bottom: 10px; }
  .contact__line { font-size: 13px; line-height: 1.6; }

  .services { position: absolute; left: 200px; top: 0; width: 360px; height: 800px; }
  .section-head { background: var(--navy); font-size: 24px; font-weight: 400; padding: 10px 18px; }
  .services__intro { font-size: 13px; line-height: 1.45; padding: 12px 18px 6px; }
  .chev-list { list-style: none; padding: 4px 18px 12px; }
  .chev-list li { position: relative; padding-left: 14px; font-size: 13px; line-height: 1.45; margin-bottom: 5px; }
  .chev-list li::before { content: "›"; position: absolute; left: 0; top: -1px; font-weight: 600; font-size: 15px; }
  .feature-list li { font-size: 15px; margin-bottom: 3px; }
</style>
</head>
<body>

<section class="page page--front">
  <div class="hero-photo" role="img" aria-label="Photo of a hand holding a glowing globe surrounded by floating business images"></div>
  <div class="hero-band"></div>
  <div class="about">
    <h2 class="about__title">About the Company</h2>
    <p class="about__text">Tidewell Systems is your partner in both affordable Computer Support and the worthwhile achievements of your business. With personalized Network Services, you can get best-fit solutions at competitive prices.</p>
    <p class="about__text">Tidewell Systems provides Computer Support that will allow you to harness the power of technology, for a predictable monthly cost. Offering service to businesses in Chicago, Wheaton, Bloomingdale, Schaumburg, Addison, Carol Stream and Elmhurst, our Computer Support can help you achieve balance between your technology and your budget.</p>
  </div>
  <svg class="front-foot" viewBox="0 0 544 120" preserveAspectRatio="none" aria-hidden="true">
    <path d="M0 105 Q 260 25 544 8 L544 120 L0 120 Z" fill="#ffffff"/>
    <path d="M0 105 Q 260 25 544 8" fill="none" stroke="#d8dde2" stroke-width="3"/>
  </svg>
  <div class="brand">
    <span class="brand__mark"></span>
    <span class="brand__name">Tidewell</span>
  </div>
</section>

<section class="page page--back">
  <div class="side-photo" role="img" aria-label="Photo of a businesswoman in a white blouse in front of a light blue digital interface"></div>
  <div class="contact">
    <h3 class="contact__title">Contact Us</h3>
    <p class="contact__line">Tidewell Systems, Inc.</p>
    <p class="contact__line">480 Harbor Crest Dr.</p>
    <p class="contact__line">Suite 210</p>
    <p class="contact__line">Lakeview, IL 60199</p>
    <p class="contact__line">Phone: 555-014-2270</p>
    <p class="contact__line">Fax: 555-014-2281</p>
  </div>

  <div class="services">
    <h2 class="section-head">Services &amp; Solutions</h2>
    <p class="services__intro">With IT products and services from Tidewell Systems, you get:</p>
    <ul class="chev-list">
      <li>Managed Services – 24/7 service with a predictable monthly payment</li>
      <li>Business Continuity Planning – disaster planning, prevention, and protection</li>
      <li>IT Consulting – you can count on our guidance and up-to-the-minute expertise</li>
      <li>Security – expert planning, implementation, auditing, monitoring, and management of complete security solutions</li>
      <li>On Demand Services – pay-as-you-go professional IT services</li>
      <li>Email / Spam Protection – stop SPAM and store your emails safely</li>
      <li>Hosted Solutions – harness the power of the Internet in order to better leverage your investment in technology</li>
      <li>Industry Solutions – specialized IT services for the legal and financial fields</li>
    </ul>
    <h2 class="section-head">Feature Listing</h2>
    <ul class="chev-list feature-list">
      <li>Cloud Office Suite</li>
      <li>Managed Services</li>
      <li>Business Continuity Planning</li>
      <li>IT Consulting</li>
      <li>Email/Spam Protection</li>
      <li>Hosted Solutions</li>
      <li>Unified Communications and</li>
      <li>MDM/BYOD</li>
    </ul>
  </div>
</section>

</body>
</html>
```